Flyer Design für Kosmetikerin und Visagistin gesucht
Zielgruppe
Ich bin ein Einmannbetrieb und biete Kosmetik für Frauen, Männer und Jugendliche, Visagistik, Nageldesign und Wimpernverlängerun an - eine bestimmte Zielgruppe gibt es eigentlich nicht - es sollen alle angesprochen werden.
Aufgabenstellung
Ich hätte gerne einen Flyer, welcher beidseitig bedruckt wird und welchen ich dann per Postwurfsendung an die Haushalte in meiner Umgebung verteilen kann, da ich gerade mein Kosmetikstudio eröffnet habe. Auf der Vorderseite hätte ich gerne meinen Namen, Dipl. Kosmetikerin, Dipl. Make-up-Artist, Dipl. Nageldesignerin, meine Adresse (eventuell kleine Karte) und meine Telefonnummer mit dem Hinweis 'Termine nach telefonischer Vereinbarung' Und meine Mailadresse.
Weiters hätte ich gerne 'Neueröffnung', 'tolle Eröffnungsangbote bis Jahresende', 'kleines Willkommensgeschenk solange der Vorrat reicht' und den Satz 'der erste Eindruck hat keine zweite Chance' darauf. Ansonsten gilt bei der Vorderseite freie Gestaltung!
Auf der Rückseite hätte ich gerne meine Preisliste - ich lade sie mal als PDF-Datei hoch...
Ich lade auch mein Logo, meine Preisliste und ein paar Bilder hoch, die Bilder dürfen verwendet werden, denn ich habe dafür auch bezahlt - ist aber keine Pflicht - bin für jede andere Idee offen! Bevorzugten Farben sind Rosa und Pink, es darf auch versielt sein! Das Format, ob quer, hochgestellt, gefaltet usw. ist mir eigentlich egal - die Preisliste soll nur gut leserlich sein - kann auch von der Anordnung her verändert werden.

```html
<!DOCTYPE html>
<html lang="de">
<head>
<meta charset="utf-8">
<title>Glanzmoment by Lena – Flyer</title>
<link rel="stylesheet" href="https://fonts.googleapis.com/css2?family=Roboto+Condensed:wght@400;700&family=Didact+Gothic&display=swap">
<style>
:root{
  --magenta:#a3126f;
  --pink:#cf4d9c;
  --pink-soft:#d98fbc;
  --ink:#1d1d1b;
  --paper:#ffffff;
  --stage:#ffffff;
}
*{box-sizing:border-box;margin:0;padding:0}
html,body{width:1200px;height:848px;overflow:hidden;background:var(--stage)}
body{position:relative;font-family:"Didact Gothic",sans-serif;color:var(--ink)}

.sheet{position:absolute;background:var(--paper);box-shadow:0 2px 8px rgba(0,0,0,.25);overflow:hidden}
.sheet::before,.sheet::after{content:"";position:absolute;top:0;bottom:0;background:var(--magenta);z-index:3}

/* front */
.front{left:105px;top:72px;width:480px;height:656px}
.front::before{left:0;width:11px}
.front::after{right:0;width:11px}

.brand{position:absolute;left:0;right:0;top:0;height:138px;display:flex;flex-direction:column;align-items:center;justify-content:center;gap:8px}
.brand-name{display:flex;align-items:center;gap:10px;font-family:"Roboto Condensed",sans-serif;font-weight:700;font-size:40px;color:var(--pink-soft);letter-spacing:.5px}
.brand-name .dot{width:26px;height:26px;border-radius:50%;background:var(--pink-soft)}
.brand-tag{font-family:"Roboto Condensed",sans-serif;font-weight:700;font-size:8px;color:#fff;background:var(--pink-soft);padding:1px 6px;letter-spacing:.3px}

.photo{position:absolute}
.photo-portrait{left:11px;top:138px;width:300px;height:392px;background:linear-gradient(160deg,#4a2b1e 0%,#8a5a45 35%,#d9ab92 60%,#c78d75 80%,#5a3426 100%)}
.photo-facial{left:314px;top:138px;width:155px;height:128px;background:linear-gradient(135deg,#d9d4d2,#f2ece9 50%,#caa893)}
.photo-nails{left:314px;top:269px;width:155px;height:128px;background:linear-gradient(135deg,#e6c9c4,#f5ece9 45%,#b998cf)}
.photo-orchid{left:314px;top:400px;width:155px;height:128px;background:linear-gradient(135deg,#f7f4f6,#b267b6 50%,#f1eef0)}

.quote{position:absolute;left:26px;top:150px;font-family:"Roboto Condensed",sans-serif;font-weight:700;font-size:23px;line-height:1.15;color:#fff;letter-spacing:.3px}

.badge{position:absolute;left:40px;top:455px;width:96px;height:96px;border-radius:50%;background:var(--magenta);color:#fff;display:flex;align-items:center;justify-content:center;text-align:center;font-family:"Roboto Condensed",sans-serif;font-weight:700;font-size:13px;line-height:1.12;z-index:2}

.hours{position:absolute;left:160px;top:538px;font-size:7.6px;line-height:1.3}
.label{font-family:"Roboto Condensed",sans-serif;font-weight:700;color:var(--magenta);font-size:8px}
.owner{position:absolute;left:325px;top:532px;font-size:7.6px;line-height:1.35}
.owner .name{font-family:"Roboto Condensed",sans-serif;font-weight:700;font-size:8.5px}
.owner .gap{margin-top:8px}

.opening{position:absolute;left:30px;top:578px}
.opening-title{font-family:"Roboto Condensed",sans-serif;font-weight:700;font-size:41px;line-height:1;color:var(--magenta);letter-spacing:.5px}
.opening-sub{font-family:"Roboto Condensed",sans-serif;font-weight:700;font-size:16.5px;line-height:1.2;color:var(--pink);margin-top:3px}

/* back */
.back{left:644px;top:133px;width:450px;height:638px}
.back::before{left:0;width:8px}
.back::after{right:0;width:8px}

.price-col{position:absolute;top:14px;font-size:6.5px;line-height:9px}
.price-col.left{left:31px;width:183px}
.price-col.right{left:239px;width:191px}
.group{margin-bottom:9px}
.group h3{font-weight:400;font-size:6.5px;color:var(--pink)}
.group h4{font-weight:700;font-size:6.5px}
.row{display:flex;justify-content:space-between;align-items:flex-end;gap:6px}
.row .price{white-space:nowrap;text-align:right}
.row + .row.split{margin-top:9px}

.photo-relax{left:8px;right:8px;bottom:0;height:112px;background:linear-gradient(180deg,#ffffff 0%,#f4e3da 40%,#e2bfae 75%,#cfa591 100%)}
</style>
</head>
<body>

<section class="sheet front">
  <header class="brand">
    <div class="brand-name"><span class="dot"></span>Glanzmoment by Lena</div>
    <div class="brand-tag">KOSMETIK | VISAGISTIK | NAGELDESIGN | WIMPERNVERLÄNGERUNG</div>
  </header>

  <div class="photo photo-portrait" role="img" aria-label="Porträt einer Frau mit geschlossenen Augen, fliederfarbenem Lidschatten und rosa Lippen"></div>
  <div class="photo photo-facial" role="img" aria-label="Kosmetikbehandlung: Gesichtsmaske wird mit Pinsel aufgetragen"></div>
  <div class="photo photo-nails" role="img" aria-label="Gepflegte Hände mit French-Manicure vor violetten Kristallen"></div>
  <div class="photo photo-orchid" role="img" aria-label="Violette Orchidee mit Make-up-Pinseln"></div>

  <p class="quote">„DER ERSTE EINDRUCK HAT<br>KEINE ZWEITE CHANCE“</p>
  <div class="badge">Tolle<br>Eröffnungs-<br>angebote bis<br>Jahresende</div>

  <div class="hours">
    <div class="label">ÖFFNUNGSZEITEN:</div>
    <div>Termine nach telefonischer Vereinbarung</div>
  </div>

  <div class="owner">
    <div class="label">INHABERIN:</div>
    <div class="name">Miriam Falkner</div>
    <div>Dipl. Kosmetikerin</div>
    <div>Dipl. Make-up-Artist</div>
    <div>Dipl. Nageldesignerin</div>
    <div class="gap">Untere Lindengasse 7/2</div>
    <div>2304 Feldau</div>
    <div class="gap">Telefon: 0660.5550142</div>
    <div>E-Mail: glanzmoment@postfach.at</div>
  </div>

  <div class="opening">
    <div class="opening-title">NEUERÖFFNUNG</div>
    <div class="opening-sub">Und ein kleines Willkommens-<br>geschenk solange der Vorrat reicht!</div>
  </div>
</section>

<section class="sheet back">
  <div class="price-col left">
    <div class="group"><h3>Gesichtsbehandlung für Eilige</h3>
      <div class="row"><span>Reinigung, Hautanalyse, Tonic, Peeling, Maske,<br>Tagespflege</span><span class="price">25,00 €</span></div></div>
    <div class="group"><h3>Gesichtsbehandlung klassisch</h3>
      <div class="row"><span>Reinigung, Hautanalyse, Peeling, Dampf,<br>Ausreinigen, Tonic, Maske, Lippenpflege,<br>Massage, Augen- und Tagespflege</span><span class="price">38,00 €</span></div></div>
    <div class="group"><h3>Gesichtsbehandlung deluxe</h3>
      <div class="row"><span>Reinigung, Hautanalyse, Peeling, Wimpern oder<br>Augenbrauen färben, Dampf, Ausreinigen, Tonic,<br>Augenbrauen faconieren, Ampulle, Maske,<br>Lippenpflege, Massage, Augen- und Tagespflege</span><span class="price">54,00 €</span></div></div>
    <div class="group"><h3>Gesichtsbehandlung Anti-Age spezial</h3>
      <div class="row"><span>Reinigung, Hautanalyse, Peeling, Dampf,<br>Ausreinigen, Tonic, Ampulle bzw. Serum,<br>Anti-Aging-Spezialmaske oder Collagen-Vlies<br>nach Hauttyp, Lippenpflege, Augenampulle,<br>Massage, Augen- und Antiaging-Tagespflege</span><span class="price">76,00 €</span></div></div>
    <div class="group"><h3>Microdermabrasionbehandlung</h3>
      <div class="row"><span>Reinigung, Peeling, Microdermabrasion,<br>Dampf, Ausreinigen, Ampulle od. Serum,<br>Maske, Augen- und Tagespflege</span><span class="price">54,00 €</span></div>
      <div class="row"><span>Microdermabrasion-Kur, 4x, mit Wochenabstand</span><span class="price">206,00 €</span></div></div>
    <div class="group"><h3>Fruchtsäurebehandlung</h3>
      <div class="row"><span>Reinigung, Peeling, AHA-Fruchtsäuretonic,<br>AHA-Gingkosomengel, Milchsäurevlies,<br>Massage mit Vit.C-Creme, Augen- und Tagespflege</span><span class="price">64,00 €</span></div>
      <div class="row"><span>Kur, 4x, mit Wochenabstand</span><span class="price">245,00 €</span></div></div>
    <div class="group"><h3>Microdermabrasion mit Fruchtsäure kombiniert</h3>
      <div class="row"><span>Reinigung, Peeling, Microdermabrasion,<br>AHA-Fruchtsäuretonic, AHA-Gingkosomengel,<br>Milchsäure-Vlies, Massage mit Vitamin-C-Creme,<br>Augen- und Tagespflege</span><span class="price">105,00 €</span></div>
      <div class="row"><span>Kur, 4x, mit Wochenabstand</span><span class="price">400,00 €</span></div></div>
    <div class="group"><h3>Aknespezialbehandlung</h3>
      <div class="row"><span>Reinigung, Peeling, Dampf, Ausreinigen, Tonic,<br>Ampulle, Aknespezialmaske, Hochfrequenz,<br>Spezialtagespflege</span><span class="price">38,00 €</span></div></div>
    <div class="group"><h3>Pigmentfleckenspezialbehandlung</h3>
      <div class="row"><span>Reinigung, Peeling, Dampf, Spezialserum,<br>Spezialmaske gegen Pigmentflecken,<br>Augenpflege, Spezialtagespflege</span><span class="price">48,00 €</span></div></div>
    <div class="group"><h3>Anticouperosespezialbehandlung</h3>
      <div class="row"><span>Reinigung, Peeling, Dampf, Spezialserum,<br>Spezialmaske, Augenpflege, Spezialtagespflege</span><span class="price">48,00 €</span></div>
      <div class="row"><span>Gesicht-, Hals- und Dekolletémassage (ca. 20 min)</span><span class="price">18,00 €</span></div>
      <div class="row"><span>Kosmetische Lymphdrainage (ca. 30 min)</span><span class="price">23,00 €</span></div></div>
  </div>

  <div class="price-col right">
    <div class="group"><h3>Zusatzbehandlungen</h3>
      <div class="row"><span>Wimpern färben</span><span class="price">6,00 €</span></div>
      <div class="row"><span>Augenbrauen färben</span><span class="price">5,00 €</span></div>
      <div class="row"><span>Augenbrauen faconnieren/harzen</span><span class="price">4,00 €</span></div>
      <div class="row"><span>Augen-Intensivbehandlung</span><span class="price">19,00 €</span></div>
      <div class="row"><span>Wimperndauerwelle</span><span class="price">18,00 €</span></div>
      <div class="row"><span>Kinn harzen</span><span class="price">6,00 €</span></div>
      <div class="row"><span>Oberlippe harzen</span><span class="price">4,00 €</span></div>
      <div class="row"><span>Wirkstoffampulle</span><span class="price">10,00 €</span></div>
      <div class="row"><span>Hochfrequenz</span><span class="price">6,00 €</span></div></div>
    <div class="group">
      <div class="row"><h3>Cellulite-/Entschlackungswickel</h3><span class="price">32,00 €</span></div>
      <div class="row"><span>10er-Block: 10+1 gratis</span><span class="price">320,00 €</span></div></div>
    <div class="group"><h3>Hände</h3>
      <div class="row"><span>Klassische Maniküre, mit Pflege oder Farb-Lack</span><span class="price">16,00 €</span></div>
      <div class="row"><span>Maniküre, mit Handpeeling und Paraffinbad</span><span class="price">32,00 €</span></div>
      <div class="row"><span>Handpeeling + Paraffinbad</span><span class="price">18,00 €</span></div>
      <div class="row split"><span>Permanenter Gel-Lack am Naturnagel</span><span class="price">16,00 €</span></div>
      <div class="row"><span>Permanent French-Manicure</span><span class="price">2,00 €</span></div>
      <div class="row"><span>Gel-Lack entfernen, mit Pflege</span><span class="price">12,00 €</span></div>
      <div class="row"><span>Nagelmodellage, mit Gel (neues Set)</span><span class="price">54,00 €</span></div>
      <div class="row"><span>Auffüllen „All inclusive“ (French, Fullcover, Glitzer;<br>Nailart/Steinchen/Airbrush/Sticker auf 2 Fingern)</span><span class="price">38,00 €</span></div>
      <div class="row"><span>Nailart/Steinchen/Airbrush/Sticker zusätzlich pro Finger</span><span class="price">0,50 €</span></div>
      <div class="row"><span>Modellage entfernen mit Pflege</span><span class="price">16,00 €</span></div></div>
    <div class="group"><h3>Permanente Wimpernverlängerung</h3>
      <div class="row"><span>Erstes Set</span><span class="price">115,00 €</span></div>
      <div class="row"><span>Auffüllen innerhalb von 3 Wochen</span><span class="price">38,00 €</span></div>
      <div class="row"><span>Innerhalb von 4–5 Wochen</span><span class="price">48,00 €</span></div></div>
    <div class="group"><h3>Enthaarung</h3>
      <div class="row"><span>Beine harzen inklusive Knie</span><span class="price">18,00 €</span></div>
      <div class="row"><span>Beine komplett harzen</span><span class="price">28,00 €</span></div>
      <div class="row"><span>Achseln harzen</span><span class="price">11,00 €</span></div>
      <div class="row"><span>Bikinizone harzen</span><span class="price">12,00 €</span></div>
      <div class="row"><span>Arme komplett harzen</span><span class="price">22,00 €</span></div>
      <div class="row"><span>Harz-Package KLEIN<br>(Beine inklusive Knien, Achseln, Bikinizone)</span><span class="price">38,00 €</span></div>
      <div class="row"><span>Harz-Package GROSS<br>(Beine, Achseln, Bikinizone, Arme)</span><span class="price">68,00 €</span></div></div>
    <div class="group"><h4>Männer:</h4>
      <div class="row"><span>Rücken harzen</span><span class="price">26,00 €</span></div>
      <div class="row"><span>Brust und Bauch harzen</span><span class="price">26,00 €</span></div></div>
    <div class="group"><h3>Make up</h3>
      <div class="row"><span>Dezentes Tages-Make-Up</span><span class="price">22,00 €</span></div>
      <div class="row"><span>Abend-Make-Up</span><span class="price">28,00 €</span></div>
      <div class="row"><span>Hochzeits-Make-Up inklusive 1 Probetermin</span><span class="price">55,00 €</span></div>
      <div class="row"><span>Braut-Package<br>(Probe-Make-Up, Make-Up am Tag der Hochzeit,<br>Nagelmodellage, Wimpernverlängerung)</span><span class="price">205,00 €</span></div></div>
  </div>

  <div class="photo photo-relax" role="img" aria-label="Entspannte Frau liegt bei einer Gesichtsbehandlung"></div>
</section>

</body>
</html>
```